Looking to design a new sign for our church.

Looking for a new sign
4 x 8 feet dimension
We are renaming the church "Medlow Ridge Community Church"
looking for legible graphics
Would like some type of backdrop being a family tree (oak) / open to other ideas as you are led
I have included a pic of the old sign for your review
would like to incorporate our Kindred Way on the lower right hand corner of the sign / see file attached

```html
<!DOCTYPE html>
<html lang="en">
<head>
<meta charset="utf-8">
<title>Medlow Ridge Community Church – Sign</title>
<link rel="stylesheet" href="https://fonts.googleapis.com/css2?family=Cinzel:wght@400;500&display=swap">
<style>
  :root {
    --backdrop: #c6c6c6;
    --sign-blue: #2e2380;
    --sign-white: #ffffff;
    --tree-tone: #e9e8f4;
  }
  html, body {
    margin: 0;
    padding: 0;
    width: 1015px;
    height: 1200px;
    overflow: hidden;
    background: var(--backdrop);
  }
  .canvas {
    position: relative;
    width: 1015px;
    height: 1200px;
  }
  .sign {
    position: absolute;
    left: 40px;
    top: 366px;
    width: 935px;
    height: 467px;
    background: var(--sign-blue);
    box-shadow: 6px 10px 14px rgba(0, 0, 0, 0.45);
    color: var(--sign-white);
    font-family: "Cinzel", serif;
  }
  .oak-tree {
    position: absolute;
    left: 340px;
    top: 32px;
    width: 255px;
    height: 190px;
  }
  .ministry-mark {
    position: absolute;
    right: 20px;
    top: 26px;
    display: flex;
    flex-direction: column;
    align-items: center;
    gap: 6px;
  }
  .ministry-mark .dot {
    width: 40px;
    height: 40px;
    border-radius: 50%;
    background: var(--sign-white);
  }
  .ministry-mark .name {
    font-size: 10px;
    letter-spacing: 0.08em;
    white-space: nowrap;
  }
  .church-name {
    position: absolute;
    left: 0;
    width: 100%;
    top: 252px;
    margin: 0;
    text-align: center;
    font-weight: 500;
    font-size: 96px;
    line-height: 1;
    letter-spacing: 0.01em;
    white-space: nowrap;
  }
  .name-rule {
    position: absolute;
    left: 44px;
    right: 44px;
    top: 366px;
    height: 2px;
    background: var(--sign-white);
  }
  .church-type {
    position: absolute;
    left: 0;
    width: 100%;
    top: 384px;
    margin: 0;
    text-align: center;
    font-weight: 400;
    font-size: 48px;
    line-height: 1;
    letter-spacing: 0.34em;
    text-indent: 0.34em;
    white-space: nowrap;
  }
</style>
</head>
<body>
<div class="canvas">
  <section class="sign">
    <svg class="oak-tree" viewBox="0 0 255 190" role="img" aria-label="White illustration of a broad oak tree">
      <ellipse cx="127" cy="88" rx="127" ry="88" fill="var(--tree-tone)"/>
      <rect x="40" y="187" width="175" height="2" fill="var(--tree-tone)"/>
    </svg>
    <div class="ministry-mark">
      <span class="dot"></span>
      <span class="name">Kindred Way</span>
    </div>
    <h1 class="church-name">Medlow Ridge</h1>
    <div class="name-rule"></div>
    <p class="church-type">Community Church</p>
  </section>
</div>
</body>
</html>
```